kestrel home systems HERS

Looking for business card design that represents our company. we are kestrel home systems and we dedicate our skills of home energy efficiency to our customer by providing energy solution to their energy problems.
HVAC
SOLAR
INSULLATION
LIGHTING
DUCT TESTING
HERS RATING.

```html
<!DOCTYPE html>
<html lang="en">
<head>
<meta charset="utf-8">
<title>Kestrel Home Systems – Business Card</title>
<link rel="stylesheet" href="https://fonts.googleapis.com/css2?family=Gentium+Book+Plus&family=Open+Sans:wght@400;800&display=swap">
<style>
  :root {
    --page: #ffffff;
    --stage: #eeeeee;
    --card: #666666;
    --band: #202020;
    --strip: #222222;
    --tag-band: #5f5f5f;
    --ink-dark: #1e1e1e;
    --ink-light: #ffffff;
    --brand-faint: #4b4b4b;
    --brand-back: #b8b8b8;
    --accent-blue: #2fa0d6;
    --accent-green: #7ea04a;
    --panel: #2a2a2a;
    --rule: #cfcfcf;
  }
  * { margin: 0; padding: 0; box-sizing: border-box; }
  html, body { width: 1200px; height: 980px; overflow: hidden; background: var(--page); }
  .stage { position: absolute; left: 17px; top: 17px; width: 1156px; height: 938px; background: var(--stage); }
  .card-shadow { position: absolute; width: 515px; background: #000; filter: blur(6px); opacity: .95; }
  .card { position: absolute; left: 355px; width: 515px; height: 309px; background: var(--card); overflow: hidden; font-family: "Gentium Book Plus", "Palatino Linotype", serif; }
  .card--front { top: 169px; }
  .card--back { top: 539px; }
  .abs { position: absolute; }
  .brand-faint { right: 8px; top: 10px; text-align: right; font-family: "Open Sans", Arial, sans-serif; font-weight: 400; color: var(--brand-faint); line-height: 1; letter-spacing: 1px; }
  .brand-faint .l1 { font-size: 40px; display: block; }
  .brand-faint .l2 { font-size: 30px; display: block; margin-top: 4px; }
  .contact-band { left: 0; top: 165px; width: 515px; height: 88px; background: var(--band); }
  .brand-dot { left: 60px; top: 112px; width: 84px; height: 84px; border-radius: 50%; background: var(--accent-blue); }
  .holder-name { left: 213px; top: 133px; font-family: "Open Sans", Arial, sans-serif; font-weight: 800; font-size: 36px; color: var(--ink-dark); line-height: 1; }
  .position { left: 0; width: 656px; top: 169px; text-align: center; color: var(--ink-light); font-size: 17px; }
  .rule { height: 1.5px; background: var(--rule); top: 181px; }
  .rule--left { left: 159px; width: 52px; }
  .rule--right { left: 446px; width: 61px; }
  .contact { color: var(--ink-light); font-size: 11.5px; letter-spacing: .3px; white-space: nowrap; }
  .tel { left: 157px; top: 202px; }
  .email { left: 309px; top: 201px; }
  .web { left: 0; width: 590px; text-align: center; top: 222px; }
  .tag-band { left: 0; top: 253px; width: 515px; height: 28px; background: var(--tag-band); }
  .tagline-front { left: 0; width: 516px; top: 256px; text-align: center; font-size: 15px; color: var(--ink-dark); letter-spacing: .4px; }
  .bottom-strip { left: 0; top: 281px; width: 515px; height: 28px; background: var(--strip); }
  .brand-panel { left: 49px; top: 87px; width: 417px; height: 135px; background: var(--panel); border: 2px solid var(--accent-green); border-radius: 6px; display: flex; flex-direction: column; align-items: center; justify-content: center; font-family: "Open Sans", Arial, sans-serif; font-weight: 400; color: var(--brand-back); line-height: 1; letter-spacing: 1px; }
  .brand-panel .l1 { font-size: 40px; }
  .brand-panel .l2 { font-size: 32px; margin-top: 8px; }
  .back-band { left: 0; top: 241px; width: 515px; height: 35px; background: #1c1c1c; }
  .tagline-back { left: 0; width: 526px; top: 249px; text-align: center; font-size: 15px; color: var(--ink-light); letter-spacing: .4px; }
</style>
</head>
<body>
<div class="stage"></div>

<div class="card-shadow" style="left:335px; top:199px; height:290px;"></div>
<section class="card card--front">
  <div class="abs brand-faint"><span class="l1">KESTREL HOME</span><span class="l2">SYSTEMS</span></div>
  <div class="abs contact-band"></div>
  <div class="abs brand-dot"></div>
  <div class="abs holder-name">Your Name</div>
  <div class="abs rule rule--left"></div>
  <div class="abs position">Position</div>
  <div class="abs rule rule--right"></div>
  <div class="abs contact tel">Tel: +41 (0) 62 555 01 47</div>
  <div class="abs contact email">Email: hello@kestrelhome.com</div>
  <div class="abs contact web">www.kestrelhome.com</div>
  <div class="abs tag-band"></div>
  <div class="abs tagline-front">Your Bussines Tagline</div>
  <div class="abs bottom-strip"></div>
</section>

<div class="card-shadow" style="left:335px; top:569px; height:290px;"></div>
<section class="card card--back">
  <div class="abs brand-panel"><span class="l1">KESTREL HOME</span><span class="l2">SYSTEMS</span></div>
  <div class="abs back-band"></div>
  <div class="abs tagline-back">Your Company Tag line</div>
</section>
</body>
</html>
```